Weihnachtskarte für Unternehmensverbund
Zielgruppe
Wir sind ein Unternehmensverbund mit drei Schwerpunkten; Indoorspielplatz, Sport und (Event)Gastronomie
Aufgabenstellung
Wir möchten gern eine Weihnachtskarte für unsere Kunden und Geschäftspartner haben, vorzugsweise im Klappformat DIN lang quer. Innen unten, leicht transparent sollten unsere Logos sein. Der Rest innen bleibt frei. Die Vorderseite möchten wir gern gestaltet haben. Idee wäre, den Jahresübergang zu thematisieren, weil wir in 2025 Jubiläum haben (30 Jahre Sport (RLK ATHLETIX) und 20 Jahre Indoorspielplatz (Bennos Kletterhain)). Logos fügen wir bei.

```html
<!DOCTYPE html>
<html lang="de">
<head>
<meta charset="utf-8">
<title>RLK ATHLETIX – Weihnachtskarte 2025</title>
<link rel="stylesheet" href="https://fonts.googleapis.com/css2?family=Mulish:wght@700;800&display=swap">
<style>
  :root {
    --navy: #27306b;
    --navy-deep: #151f55;
    --navy-light: #2f63b8;
    --gold-dark: #9a7430;
    --gold: #b8903f;
    --gold-light: #e6c783;
    --cream: #ead3b2;
    --cream-light: #f8eee0;
    --paper: #ffffff;
    --stage: #f2f2f2;
  }
  * { box-sizing: border-box; margin: 0; padding: 0; }
  html, body {
    width: 1200px; height: 848px; overflow: hidden;
    background: var(--stage);
    font-family: "Mulish", sans-serif;
  }
  .card {
    position: absolute; left: 20px; top: 151px;
    width: 1160px; height: 546px;
    background: var(--paper);
    overflow: hidden;
  }
  .card__balloons {
    position: absolute; inset: 0;
    width: 1160px; height: 546px;
  }
  .jubilee {
    position: absolute;
    text-align: center;
    font-weight: 800;
    line-height: 1.05;
    white-space: nowrap;
  }
  .jubilee__years { display: block; }
  .jubilee__name { display: block; margin-top: 6px; }
  .jubilee--play {
    left: 773px; top: 106px; width: 160px;
    color: var(--navy);
    transform: rotate(-18deg);
  }
  .jubilee--play .jubilee__years { font-size: 30px; }
  .jubilee--play .jubilee__name { font-size: 16px; }
  .jubilee--sport {
    left: 948px; top: 160px; width: 190px;
    color: var(--paper);
    transform: rotate(16deg);
  }
  .jubilee--sport .jubilee__years { font-size: 38px; }
  .jubilee--sport .jubilee__name { font-size: 22px; }
  .greeting {
    position: absolute; left: 0; top: 0;
    color: var(--navy);
  }
  .greeting__title {
    position: absolute; left: 210px; top: 329px;
    white-space: nowrap;
    font-size: 70px; font-weight: 700; letter-spacing: -0.3px; line-height: 1;
  }
  .greeting__sub {
    position: absolute; left: 356px; top: 402px;
    white-space: nowrap;
    font-size: 25px; font-weight: 800; line-height: 1;
  }
</style>
</head>
<body>
  <main class="card">
    <svg class="card__balloons" viewBox="0 0 1160 546" role="img" aria-label="Goldene, cremefarbene und blaue Luftballons mit goldenem Konfetti und Sternen">
      <defs>
        <radialGradient id="fill-gold" cx="0.38" cy="0.32" r="0.75">
          <stop offset="0" stop-color="var(--gold-light)"/>
          <stop offset="0.55" stop-color="var(--gold)"/>
          <stop offset="1" stop-color="var(--gold-dark)"/>
        </radialGradient>
        <radialGradient id="fill-cream" cx="0.38" cy="0.32" r="0.75">
          <stop offset="0" stop-color="var(--cream-light)"/>
          <stop offset="1" stop-color="var(--cream)"/>
        </radialGradient>
        <radialGradient id="fill-navy" cx="0.6" cy="0.4" r="0.7">
          <stop offset="0" stop-color="var(--navy-light)"/>
          <stop offset="0.55" stop-color="var(--navy)"/>
          <stop offset="1" stop-color="var(--navy-deep)"/>
        </radialGradient>
        <g id="balloon-shape">
          <path d="M0,-1 C0.58,-1 1,-0.58 1,-0.08 C1,0.45 0.5,0.94 0,0.98 C-0.5,0.94 -1,0.45 -1,-0.08 C-1,-0.58 -0.58,-1 0,-1 Z"/>
          <path d="M-0.09,1.07 L0.09,1.07 L0,0.96 Z"/>
        </g>
        <ellipse id="balloon-shine" cx="-0.38" cy="-0.5" rx="0.16" ry="0.26" fill="#ffffff" opacity="0.45" transform="rotate(30 -0.38 -0.5)"/>
      </defs>

      <g fill="url(#fill-gold)">
        <g transform="translate(154 67) scale(88 98)"><use href="#balloon-shape"/><use href="#balloon-shine"/></g>
        <g transform="translate(1029 53) scale(90 110)"><use href="#balloon-shape"/><use href="#balloon-shine"/></g>
        <g transform="translate(37 486) scale(80 95)"><use href="#balloon-shape"/><use href="#balloon-shine"/></g>
        <g transform="translate(281 490) scale(87 98)"><use href="#balloon-shape"/><use href="#balloon-shine"/></g>
        <g transform="translate(939 518) scale(78 92)"><use href="#balloon-shape"/><use href="#balloon-shine"/></g>
      </g>
      <g fill="url(#fill-cream)">
        <g transform="translate(30 182) scale(70 95) rotate(-10)"><use href="#balloon-shape"/><use href="#balloon-shine"/></g>
        <g transform="translate(91 395) scale(88 95) rotate(-12)"><use href="#balloon-shape"/><use href="#balloon-shine"/></g>
        <g transform="translate(439 504) scale(80 95)"><use href="#balloon-shape"/><use href="#balloon-shine"/></g>
        <g transform="translate(1122 464) scale(60 120)"><use href="#balloon-shape"/><use href="#balloon-shine"/></g>
      </g>
      <g fill="url(#fill-gold)" transform="translate(853 161) rotate(-14) scale(92 116)">
        <use href="#balloon-shape"/><use href="#balloon-shine"/>
      </g>
      <g fill="url(#fill-navy)" transform="translate(1043 219) rotate(12) scale(106 132)">
        <use href="#balloon-shape"/>
      </g>
    </svg>

    <div class="jubilee jubilee--play">
      <span class="jubilee__years">20 JAHRE</span>
      <span class="jubilee__name">BENNOS<br>KLETTERHAIN</span>
    </div>
    <div class="jubilee jubilee--sport">
      <span class="jubilee__years">30 JAHRE</span>
      <span class="jubilee__name">RLK ATHLETIX</span>
    </div>

    <section class="greeting">
      <h1 class="greeting__title">Frohe Weihnachten</h1>
      <p class="greeting__sub">...UND EINEN GUTEN START INS NEUE JAHR 2025!</p>
    </section>
  </main>
</body>
</html>
```